Business is backhoe and truck hire. As the title indicates, we dig dirt. Colours preferred are charcoal, red and or orange. Would like a backhoe on the card,possibly a designs with the silhouette of the machine in the background. I We would like to incorporate a large tick in the title for solutions. I thought it could be part of the "W" . Our shirts are Black polo's with orange lines around sleeves and sides. We are a new business in rural Qld, happy to do the smaller jobs that others wont.

Industry/Entity Type

Business

Contact Information for Business Card

Tall Creek Groundworks Services

Backhoe and Truck Hire
ABN:81264950173

Peter Holloway
PH: 0491 732 580
PH: 0493 618 204
PH: 4683 1057 a/h

email: tcgservices@mailbox-example.net

```html
<!DOCTYPE html>
<html lang="en">
<head>
<meta charset="utf-8">
<title>Tall Creek Groundworks Services – Business Card</title>
<link rel="stylesheet" href="https://fonts.googleapis.com/css2?family=Oswald:wght@600;700&family=Archivo+Black&display=swap">
<style>
  :root {
    --charcoal: #4a4a51;
    --charcoal-light: #55555c;
    --panel: #8a5531;
    --panel-edge: #7d4c2b;
    --ink: #3b3b42;
    --machine-yellow: #f2c21b;
    --machine-dark: #2c2d30;
  }
  * { margin: 0; padding: 0; box-sizing: border-box; }
  html, body { width: 1200px; height: 695px; overflow: hidden; }
  body { background: var(--charcoal); }
  .card {
    position: relative;
    width: 1200px;
    height: 695px;
    background: radial-gradient(ellipse at 60% 45%, var(--charcoal-light), var(--charcoal) 75%);
    overflow: hidden;
  }
  .panel {
    position: absolute;
    left: 20px;
    width: 673px;
    background: var(--panel);
    box-shadow: 0 0 6px 3px var(--panel-edge), 0 10px 16px rgba(0,0,0,0.45);
    color: var(--ink);
  }
  .panel--title { top: 23px; height: 130px; }
  .panel--name { top: 251px; height: 132px; }
  .panel--contact { top: 464px; height: 202px; }

  .title-line {
    position: absolute;
    left: 68px;
    font-family: "Oswald", sans-serif;
    font-weight: 700;
    font-variant: small-caps;
    font-size: 38px;
    line-height: 1;
    letter-spacing: 0.3px;
    white-space: nowrap;
  }
  .title-line--company { top: 14px; }
  .title-line--service { top: 68px; }
  .person-name {
    position: absolute;
    left: 68px;
    top: 28px;
    font-family: "Oswald", sans-serif;
    font-weight: 700;
    font-variant: small-caps;
    font-size: 62px;
    line-height: 1;
    white-space: nowrap;
  }
  .contact-list {
    position: absolute;
    left: 31px;
    top: 10px;
    list-style: none;
    font-family: "Archivo Black", sans-serif;
    font-size: 30px;
    line-height: 38px;
    white-space: nowrap;
  }
  .contact-list .after-hours { font-variant: small-caps; font-size: 24px; }
  .contact-list .email { font-variant: small-caps; font-size: 24px; line-height: 40px; text-transform: lowercase; }

  .machine-art {
    position: absolute;
    left: 721px;
    top: 192px;
    width: 451px;
    height: 330px;
  }
</style>
</head>
<body>
<main class="card">
  <section class="panel panel--title">
    <h1 class="title-line title-line--company">Tall Creek Groundworks Services</h1>
    <p class="title-line title-line--service">Backhoe and Truck Hire</p>
  </section>

  <section class="panel panel--name">
    <h2 class="person-name">Peter Holloway</h2>
  </section>

  <section class="panel panel--contact">
    <ul class="contact-list">
      <li>ABN:81264950173</li>
      <li>PH: 0491 732 580</li>
      <li>PH: 0493 618 204</li>
      <li>PH: 4683 1057 <span class="after-hours">a/h</span></li>
      <li class="email">email: tcgservices@mailbox-example.net</li>
    </ul>
  </section>

  <svg class="machine-art" viewBox="0 0 451 330" role="img" aria-label="Yellow backhoe loader illustration">
    <defs>
      <linearGradient id="machineFill" x1="0" y1="0" x2="1" y2="1">
        <stop offset="0" stop-color="var(--machine-yellow)"/>
        <stop offset="0.6" stop-color="#d9a814"/>
        <stop offset="1" stop-color="var(--machine-dark)"/>
      </linearGradient>
    </defs>
    <rect x="0" y="0" width="451" height="330" rx="18" fill="url(#machineFill)" opacity="0.85"/>
  </svg>
</main>
</body>
</html>
```